Flyer design for mailer

I want to take the attached information and make it look pretty in a similar fashion to our website > www.brelmont.com for a mailer.
The final size should fit in a 6x9 envelope. Looking for a front and back. And QR code to our website.

```html
<!DOCTYPE html>
<html lang="en">
<head>
<meta charset="utf-8">
<title>Brelmont Solutions Mailer</title>
<link href="https://fonts.googleapis.com/css2?family=Montserrat:ital,wght@0,400;0,500;0,700;0,800;1,600&display=swap" rel="stylesheet">
<style>
:root{
  --navy:#163f73;
  --deep-blue:#123a6b;
  --sky:#0aa0dc;
  --pale-blue:#cfe0ef;
  --mid-blue:#3f9ad6;
  --maroon:#8e1b1c;
  --ink:#222;
  --white:#fff;
  --backdrop:#b4b4b4;
}
*{margin:0;padding:0;box-sizing:border-box}
html,body{width:1200px;height:1117px;overflow:hidden}
body{background:var(--backdrop);font-family:"Montserrat",sans-serif;position:relative}
.page{position:absolute;top:224px;width:518px;height:669px;background:var(--white);overflow:hidden;box-shadow:0 4px 10px rgba(0,0,0,.25)}
.page--front{left:66px}
.page--back{left:616px}
.top-band{position:absolute;left:0;top:0;width:100%;height:16px;background:var(--navy)}

/* front */
.hero-art{position:absolute;left:0;top:27px;width:100%;height:504px;
  background:radial-gradient(circle at 50% 48%,#bfe3f5 0,#3d8fc4 18%,#1c5f94 45%,#0f3763 100%)}
.front-lower{position:absolute;left:0;top:531px;width:100%;height:349px;background:linear-gradient(180deg,#3b94d2,#2f86c8)}
.logo-tab{position:absolute;left:115px;top:0;width:287px;height:106px;background:var(--white);
  clip-path:polygon(0 0,100% 0,88% 88%,82% 100%,18% 100%,12% 88%);display:flex;align-items:center;justify-content:center;gap:8px}
.brand-mark{width:14px;height:14px;background:var(--maroon)}
.brand-name{color:var(--maroon);font-weight:800;font-size:21px;line-height:1.05;text-transform:uppercase;letter-spacing:.5px}
.hello-card{position:absolute;left:31px;top:460px;width:456px;height:131px;background:var(--white);border-radius:12px;padding:14px 22px}
.hello-card h1{color:var(--maroon);font-size:27px;font-weight:800;line-height:1}
.hello-card p{margin-top:6px;font-size:12.6px;line-height:17.5px;color:var(--ink)}
.hello-card strong{font-weight:700}
.front-web{position:absolute;left:0;top:612px;width:100%;text-align:center;color:var(--white);font-size:18px;font-weight:500}
.front-web b{font-weight:800}
.bottom-strip{position:absolute;left:0;bottom:0;width:100%;height:13px;background:var(--white)}

/* back */
.back-field{position:absolute;left:0;top:16px;width:100%;height:472px;background:var(--pale-blue)}
.team-photo{position:absolute;left:255px;top:37px;width:263px;height:403px;
  background:linear-gradient(135deg,#5c6c5a 0%,#3c4438 45%,#20262a 100%)}
.tools-card{position:absolute;left:30px;top:37px;width:237px;height:403px;background:var(--white);border-radius:12px;padding:22px 0 0 15px}
.tools-pill{width:204px;height:25px;border-radius:13px;background:var(--maroon);color:var(--white);font-weight:800;font-size:13px;display:flex;align-items:center;justify-content:center}
.tools-list{list-style:none;margin-top:9px}
.tools-list li{position:relative;padding-left:19px;font-size:13px;line-height:20px;color:var(--ink)}
.tools-list svg{position:absolute;left:0;top:5px;width:11px;height:11px}
.cta-box{position:absolute;left:30px;top:467px;width:456px;height:64px;border-radius:6px;background:var(--sky);color:var(--white);font-weight:800;font-size:15.5px;line-height:20px;text-align:center;display:flex;align-items:center;justify-content:center;padding:0 20px}
.thanks{position:absolute;left:0;top:543px;width:100%;text-align:center;color:var(--deep-blue);font-weight:800;font-size:13.6px}
.signoff{position:absolute;left:43px;top:586px}
.signoff .name{color:var(--maroon);font-weight:800;font-size:26px;line-height:1}
.signoff .title{color:var(--sky);font-style:italic;font-weight:600;font-size:14.5px;margin-top:2px}
.back-brand{position:absolute;top:596px;display:flex;align-items:center;gap:5px}
.back-brand .brand-mark{width:10px;height:10px}
.back-brand .brand-name{font-size:14px}
.back-brand--solutions{left:233px}
.back-brand--view{left:374px}
.back-brand--view .brand-name{font-size:20px;text-transform:none}
.back-strip{position:absolute;left:0;bottom:0;width:100%;height:13px;background:var(--pale-blue)}
</style>
</head>
<body>

<section class="page page--front">
  <div class="hero-art" role="img" aria-label="Photo of a hand touching a glowing cloud icon linked to security, people, chart, settings and server icons"></div>
  <div class="front-lower"></div>
  <div class="top-band"></div>
  <div class="logo-tab">
    <span class="brand-mark"></span>
    <span class="brand-name">Brelmont<br>Solutions</span>
  </div>
  <div class="hello-card">
    <h1>Hello!</h1>
    <p>Now that I’ve got my foot in the door, I wanted to kick off a quick chat about how we’ve helped <strong>1,200+ K-12</strong> school districts digitize <strong>900 million records</strong> and move toward paperless operations with our cloud-based tools.</p>
  </div>
  <div class="front-web">www.<b>brelmontsolutions</b>.com</div>
  <div class="bottom-strip"></div>
</section>

<section class="page page--back">
  <div class="back-field"></div>
  <div class="top-band"></div>
  <div class="team-photo" role="img" aria-label="Photo of two colleagues working together at a computer"></div>
  <div class="tools-card">
    <div class="tools-pill">WE HAVE TOOLS FOR:</div>
    <ul class="tools-list">
      <li><svg viewBox="0 0 12 12"><circle cx="6" cy="6" r="6" fill="#0aa0dc"/><path d="M3.3 6.2l1.8 1.8 3.6-3.8" fill="none" stroke="#fff" stroke-width="1.6"/></svg>Transcripts</li>
      <li><svg viewBox="0 0 12 12"><circle cx="6" cy="6" r="6" fill="#0aa0dc"/><path d="M3.3 6.2l1.8 1.8 3.6-3.8" fill="none" stroke="#fff" stroke-width="1.6"/></svg>Hiring</li>
      <li><svg viewBox="0 0 12 12"><circle cx="6" cy="6" r="6" fill="#0aa0dc"/><path d="M3.3 6.2l1.8 1.8 3.6-3.8" fill="none" stroke="#fff" stroke-width="1.6"/></svg>Onboarding/Offboarding</li>
      <li><svg viewBox="0 0 12 12"><circle cx="6" cy="6" r="6" fill="#0aa0dc"/><path d="M3.3 6.2l1.8 1.8 3.6-3.8" fill="none" stroke="#fff" stroke-width="1.6"/></svg>Maintenance Requests</li>
      <li><svg viewBox="0 0 12 12"><circle cx="6" cy="6" r="6" fill="#0aa0dc"/><path d="M3.3 6.2l1.8 1.8 3.6-3.8" fill="none" stroke="#fff" stroke-width="1.6"/></svg>Timesheets</li>
      <li><svg viewBox="0 0 12 12"><circle cx="6" cy="6" r="6" fill="#0aa0dc"/><path d="M3.3 6.2l1.8 1.8 3.6-3.8" fill="none" stroke="#fff" stroke-width="1.6"/></svg>Substitute Management</li>
      <li><svg viewBox="0 0 12 12"><circle cx="6" cy="6" r="6" fill="#0aa0dc"/><path d="M3.3 6.2l1.8 1.8 3.6-3.8" fill="none" stroke="#fff" stroke-width="1.6"/></svg>Professional Development Tracking</li>
      <li><svg viewBox="0 0 12 12"><circle cx="6" cy="6" r="6" fill="#0aa0dc"/><path d="M3.3 6.2l1.8 1.8 3.6-3.8" fill="none" stroke="#fff" stroke-width="1.6"/></svg>Expense Reports (integrated with RouteMap)</li>
      <li><svg viewBox="0 0 12 12"><circle cx="6" cy="6" r="6" fill="#0aa0dc"/><path d="M3.3 6.2l1.8 1.8 3.6-3.8" fill="none" stroke="#fff" stroke-width="1.6"/></svg>We can make any paper process completely electronic with customized Workflows</li>
      <li><svg viewBox="0 0 12 12"><circle cx="6" cy="6" r="6" fill="#0aa0dc"/><path d="M3.3 6.2l1.8 1.8 3.6-3.8" fill="none" stroke="#fff" stroke-width="1.6"/></svg>And we are developing more every year!</li>
    </ul>
  </div>
  <div class="cta-box">Please reach out at DMarlow@BrelView.com or give me a call on my cell at 555-014-2270.</div>
  <div class="thanks">Thank you, and I can’t wait to take the next step with you!</div>
  <div class="signoff">
    <div class="name">Dana Marlow</div>
    <div class="title">Account Executive</div>
  </div>
  <div class="back-brand back-brand--solutions"><span class="brand-mark"></span><span class="brand-name">Brelmont<br>Solutions</span></div>
  <div class="back-brand back-brand--view"><span class="brand-mark"></span><span class="brand-name">BrelView</span></div>
  <div class="back-strip"></div>
</section>

</body>
</html>
```